Envelope Design Project for Real Estate

I am looking for an envelope design for a real estate brokerage. I prefer muted colors and the primary colors should be white, maroon (884445) and gray (aaaaaa).
The design is for a #10 universal envelope (psd and jpg files attached for guidelines). There should be full color on the front and back of the envelope.
You can add a return address on the back side along the top flap. Please use a sample address and phone number in the design - the actual information will be provided to the winning designer.

```html
<!DOCTYPE html>
<html lang="en">
<head>
<meta charset="utf-8">
<title>Harbor Birch Realty — Envelope Front</title>
<link rel="stylesheet" href="https://fonts.googleapis.com/css2?family=Libre+Baskerville:wght@400&display=swap">
<style>
  :root {
    --maroon: #7b2a42;
    --white: #ffffff;
    --gray: #9c8f93;
    --serif: "Libre Baskerville", "Baskerville", Georgia, serif;
  }
  html, body {
    margin: 0;
    padding: 0;
    overflow: hidden;
    background: var(--maroon);
  }
  .envelope {
    position: relative;
    width: 1200px;
    height: 523px;
    background: var(--maroon);
    font-family: var(--serif);
    color: var(--white);
    overflow: hidden;
  }
  .brand {
    position: absolute;
    left: 42px;
    top: 44px;
    width: 208px;
    height: 190px;
    display: flex;
    flex-direction: column;
    align-items: center;
    justify-content: center;
    gap: 18px;
  }
  .brand-mark {
    width: 46px;
    height: 46px;
    background: var(--white);
  }
  .brand-name {
    margin: 0;
    font-size: 30px;
    font-weight: 400;
    line-height: 1.15;
    text-align: center;
    color: var(--white);
  }
  .sender {
    position: absolute;
    left: 33px;
    top: 393px;
    text-transform: uppercase;
    line-height: 1;
  }
  .sender-name {
    font-size: 17px;
    margin: 0 0 6px;
  }
  .sender-title {
    font-size: 13.5px;
    color: var(--gray);
    margin: 0 0 7px;
  }
  .sender-email {
    font-size: 17px;
    margin: 0 0 5px;
  }
  .contact-line {
    position: relative;
    height: 16px;
    font-size: 14px;
    white-space: nowrap;
  }
  .contact-line span {
    position: absolute;
    top: 0;
  }
</style>
</head>
<body>
  <main class="envelope">
    <div class="brand">
      <div class="brand-mark" aria-hidden="true"></div>
      <p class="brand-name">Harbor Birch<br>Realty</p>
    </div>

    <section class="sender">
      <p class="sender-name">Daniel Hargrove</p>
      <p class="sender-title">Principal Broker and Owner</p>
      <p class="sender-email">daniel@harborbirchhomes.com</p>
      <div class="contact-line">
        <span style="left:0">(410) 555-0142</span>
        <span style="left:127px">Mobile|</span>
        <span style="left:253px">(443) 555-0178</span>
        <span style="left:380px">Office &nbsp;|</span>
        <span style="left:506px">(443) 555-0193</span>
        <span style="left:633px">Fax</span>
      </div>
    </section>
  </main>
</body>
</html>
```